Customs House descriptive business cards

We require a two-sided business card that has a simple yet elegant design. We want to be able to promote our services as a customs house. This card should include our logo, contact info and services offered with the logo being on one side and the contact info and services on the flip side

Target Market(s)

Importers / exporters to and from the Bahamas

Industry/Entity Type

Logistics

Contact Information for Business Card

The front side of the card could have the logo and the flip side should have the other relevant info

Font styles to use
Serif

Colors

Designer to choose colors to be used in the design.

Requirements
Must have
• (Kelpway Brokers Ltd) Logo, address and contact info also services:
• import customs clearance, Delivery & HAndling services,Florida pickups, Export packing & Crating Services, export customs clearance, Consulting

```html
<!DOCTYPE html>
<html lang="en">
<head>
<meta charset="UTF-8">
<title>Kelpway Brokers Ltd – Business Card</title>
<link href="https://fonts.googleapis.com/css2?family=Libre+Baskerville:wght@400;700&family=Roboto:wght@400&display=swap" rel="stylesheet">
<style>
  :root {
    --page-bg: #dcdcdc;
    --card-bg: #eef0f3;
    --card-edge: #c9ced6;
    --brand-blue: #1f4f93;
    --title-grey: #7a7f87;
    --text-dark: #2b2e33;
    --band-top: #23548f;
    --band-bottom: #12356b;
    --band-text: #d9dee7;
    --band-bullet: #e8899a;
    --divider: #8a8f96;
  }
  * { margin: 0; padding: 0; box-sizing: border-box; }
  html, body { width: 1200px; height: 969px; overflow: hidden; }
  body { background: var(--page-bg); position: relative; font-family: "Roboto", Arial, sans-serif; }

  .card {
    position: absolute; left: 100px; top: 199px;
    width: 1000px; height: 570px;
    background: var(--card-bg);
    border: 1px solid var(--card-edge);
    box-shadow: 0 10px 30px rgba(0,0,0,0.15);
  }

  .brand {
    position: absolute; left: 80px; top: 100px; width: 424px;
    display: flex; flex-direction: column; align-items: center;
  }
  .brand-mark {
    width: 170px; height: 170px; border-radius: 50%;
    background: var(--brand-blue);
  }
  .brand-name {
    margin-top: 40px;
    font-family: "Roboto", Arial, sans-serif; font-weight: 400;
    font-size: 36px; color: var(--brand-blue); white-space: nowrap;
  }

  .divider {
    position: absolute; left: 488px; top: 88px;
    width: 1px; height: 300px; background: var(--divider);
  }

  .contact { position: absolute; left: 534px; top: 90px; }
  .person-name {
    font-family: "Libre Baskerville", Georgia, serif; font-weight: 700;
    font-size: 34px; color: var(--brand-blue); line-height: 1.1;
  }
  .person-title {
    font-family: "Libre Baskerville", Georgia, serif;
    font-size: 21px; color: var(--title-grey); margin-top: 2px;
  }
  .address { font-size: 23px; color: var(--text-dark); line-height: 29px; margin-top: 26px; }
  .details { list-style: none; margin-top: 20px; }
  .details li {
    display: flex; align-items: center; gap: 14px;
    font-size: 23px; color: var(--text-dark); height: 32px;
  }
  .details svg { width: 20px; height: 20px; fill: var(--brand-blue); flex: none; }

  .services-band {
    position: absolute; left: 0; top: 439px; width: 100%; height: 96px;
    background: linear-gradient(180deg, var(--band-top), var(--band-bottom));
    display: flex; flex-direction: column; justify-content: center; align-items: center;
    color: var(--band-text); font-size: 23px; line-height: 30px;
  }
  .services-band .dot { color: var(--band-bullet); margin: 0 6px; }
</style>
</head>
<body>
  <div class="card">
    <div class="brand">
      <div class="brand-mark"></div>
      <div class="brand-name">Kelpway Brokers Ltd</div>
    </div>

    <div class="divider"></div>

    <div class="contact">
      <div class="person-name">AARON HALE</div>
      <div class="person-title">CEO/FOUNDER</div>
      <p class="address">214 Harbor Reach Road<br>Nassau, Bahamas 10482</p>
      <ul class="details">
        <li>
          <svg viewBox="0 0 24 24"><path d="M6.6 10.8c1.4 2.8 3.8 5.1 6.6 6.6l2.2-2.2c.3-.3.7-.4 1-.2 1.1.4 2.3.6 3.6.6.6 0 1 .4 1 1V20c0 .6-.4 1-1 1C10.6 21 3 13.4 3 4c0-.6.4-1 1-1h3.5c.6 0 1 .4 1 1 0 1.3.2 2.5.6 3.6.1.3 0 .7-.2 1z"/></svg>
          555 210 4471
        </li>
        <li>
          <svg viewBox="0 0 24 24"><path d="M7 1h10c1.1 0 2 .9 2 2v18c0 1.1-.9 2-2 2H7c-1.1 0-2-.9-2-2V3c0-1.1.9-2 2-2zm0 3v14h10V4H7zm5 15.5a1 1 0 100 2 1 1 0 000-2z"/></svg>
          555 318 6620
        </li>
        <li>
          <svg viewBox="0 0 24 24"><path d="M2 5h20v14H2V5zm2 2v.5l8 5 8-5V7H4zm16 2.8l-8 5-8-5V17h16V9.8z"/></svg>
          aaron@kelpwaybrokers.com
        </li>
        <li>
          <svg viewBox="0 0 24 24"><path d="M12 2a10 10 0 100 20 10 10 0 000-20zm-1 17.9A8 8 0 014.1 10.1L9 15v1c0 1.1.9 2 2 2v1.9zm6.9-2.5c-.3-.8-1-1.4-1.9-1.4h-1v-3c0-.6-.4-1-1-1H8v-2h2c.6 0 1-.4 1-1V7h2c1.1 0 2-.9 2-2v-.4a8 8 0 012.9 12.8z"/></svg>
          www.kelpwaybrokers.com
        </li>
      </ul>
    </div>

    <div class="services-band">
      <div>Import customs clearance<span class="dot">•</span>Delivery &amp; Handling services<span class="dot">•</span>Florida pickups</div>
      <div>Export packing &amp; Crating Services<span class="dot">•</span>Export customs clearance<span class="dot">•</span>Consulting</div>
    </div>
  </div>
</body>
</html>
```